letterhead design using our existing logo

We are a small boutique property management business based in Sydney's Northern Beaches.
We are after a sleek, simple modern letterhead (A4) incorporating our logo and its colours.
Also matching envelope (DL)
I have attached the logo with black text and white text for design options.

Target Market(s)

29-69yo Male and Female

Industry/Entity Type

Property Management

Requirements
Must have
• - Estate Haven logo
• - Address, number and website:
• Suite 7, 18-19 Harlow Parade, Brenton NSW 2187
• Tel: Carl Doyle 0419 267 530 Miriam Kovacs 0407 516 948 www.estatehavenrealty.com.au
Nice to have
• sleek design that looks modern and professional
Should not have
• too many colours or too busy

```html
<!DOCTYPE html>
<html lang="en">
<head>
<meta charset="utf-8">
<title>Estate Haven Letterhead</title>
<link rel="stylesheet" href="https://fonts.googleapis.com/css2?family=Source+Sans+3:wght@400;600&display=swap">
<style>
  :root {
    --backdrop: #e6e8e9;
    --paper: #ffffff;
    --teal-deep: #0c4558;
    --teal-faint: #175a6e;
    --ink: #123f4f;
    --white: #ffffff;
  }
  html, body {
    margin: 0;
    padding: 0;
    width: 960px;
    height: 1200px;
    overflow: hidden;
    background: var(--backdrop);
    font-family: "Source Sans 3", "Myriad Pro", Arial, sans-serif;
  }
  .sheet {
    position: absolute;
    left: 60px;
    top: 6px;
    width: 840px;
    height: 1188px;
    background: var(--paper);
    box-shadow: 0 2px 10px rgba(0,0,0,0.12);
    overflow: hidden;
  }
  .header-band {
    position: absolute;
    left: 0;
    top: 0;
    width: 840px;
    height: 150px;
    background: var(--teal-deep);
  }
  .brand-block {
    position: absolute;
    right: 0;
    top: 0;
    width: 230px;
    height: 212px;
    background: var(--teal-deep);
  }
  .band-wordmark {
    position: absolute;
    left: 6px;
    top: 52px;
    margin: 0;
    font-size: 118px;
    font-weight: 600;
    letter-spacing: 2px;
    line-height: 1;
    color: var(--teal-faint);
    white-space: nowrap;
    height: 98px;
    overflow: hidden;
    text-transform: uppercase;
  }
  .brand-name {
    position: absolute;
    right: 22px;
    top: 162px;
    display: flex;
    align-items: center;
    gap: 8px;
    color: var(--white);
    font-size: 24px;
    font-weight: 600;
    letter-spacing: 0.5px;
    text-transform: uppercase;
  }
  .brand-dot {
    width: 9px;
    height: 9px;
    border-radius: 50%;
    background: var(--white);
  }
  .contact-line {
    position: absolute;
    left: 14px;
    top: 160px;
    width: 590px;
    margin: 0;
    font-size: 10.5px;
    color: var(--ink);
    white-space: nowrap;
  }
  .contact-web {
    position: absolute;
    right: 22px;
    top: 196px;
    margin: 0;
    font-size: 10.5px;
    color: var(--white);
  }
</style>
</head>
<body>
  <main class="sheet">
    <header>
      <div class="header-band"></div>
      <div class="brand-block"></div>
      <p class="band-wordmark" aria-hidden="true">Estate Haven</p>
      <p class="contact-line">Suite 7, 18-19 Harlow Parade, Brenton NSW 2187, Tel: Carl Doyle 0419 267 530, Miriam Kovacs 0407 516 948,</p>
      <div class="brand-name"><span class="brand-dot"></span>Estate Haven</div>
      <p class="contact-web">www.estatehavenrealty.com.au</p>
    </header>
  </main>
</body>
</html>
```